Scrubbing Paper Towel Company needs Label Design

We need a product label that wraps around a roll of scrubbing paper towels as a sticker label of individually wrapped rolls. The sticker label has dimensions of 11.5" x 6" (width x height). The company logo with the brand feel and color theme is attached.

This is mainly used for dishwashing. A very large section of the label should show dishwashing and cleaning. Two very similar products can be found here :
---> https://www.shopvantrel.example/Non-Scratch-Disposable-Dish-Washing-Scrubbing-KT47R/dp/Q5203LMNVA/ref=sr_1_9?keywords=scouring+sheet&qid=4802719355&sr=8-9
--->https://www.shopvantrel.example/Pilu-Fendra-Disposable-Dish-washing-Scrubbing/dp/Q5864TXHWD/ref=sr_1_15?keywords=scouring+sheet&qid=4802719355&sr=8-15

To be included in the label:

Key points:
Did you know? Sponges are the perfect place for bacteria growth! We're talking hundreds of different species of bacteria growing in your dishwashing sponge - just as bad as the inside of your toilet. So why use a dirty sponge over and over again? Why does it smell so bad? Yes your toilet is gross, but why should the sponge go overlooked?

The Quirra Wipe is a sanitary solution to this problem. Use it once, wash and reuse up to three times before throwing each sheet away - that's enough for 180 washes per roll! But don't limit yourself to dishwashing. It's great for scrubbing surfaces with hardened debris or even dry residue left from old spills. So go ahead, take a stand against bacteria and wash away knowing your kitchen is finally clean. Now that's sanitary!

Multipurpose Use:
Dishwashing
**(with example image/graphic)**
Cleaning Toilets
Cleaning Grills
Wiping Down Stoves
Cleaning Sinks
Cleaning Pet Bowls

60 Sheets
7.9" X 8.7" per sheet

Features:
Perforated for Easy Tear
Reusable
Liquid Absorbent
Non-Flammable
Cadmium Free
Kitchen Safe

```html
<!DOCTYPE html>
<html lang="en">
<head>
<meta charset="utf-8">
<title>Quirra Wipe – Roll Label</title>
<link href="https://fonts.googleapis.com/css2?family=Roboto:ital,wght@0,400;0,500;0,700;1,700&display=swap" rel="stylesheet">
<style>
  :root {
    --blue-deep: #0b1a78;
    --blue-mid: #1a33b4;
    --blue-bright: #2f56e0;
    --ink-white: #ffffff;
    --header-ink: #16247a;
    --header-fill-top: #ffffff;
    --header-fill-bottom: #c9cff0;
    --rule: rgba(255,255,255,0.85);
  }
  * { margin: 0; padding: 0; box-sizing: border-box; }
  html, body { width: 1200px; height: 626px; overflow: hidden; }
  body { font-family: "Roboto", Arial, sans-serif; color: var(--ink-white); }

  .label {
    position: relative; width: 1200px; height: 626px; overflow: hidden;
    background: linear-gradient(160deg, var(--blue-mid) 0%, var(--blue-deep) 70%, #08145c 100%);
  }
  .backdrop-photo {
    position: absolute; left: 0; top: 0; width: 760px; height: 430px;
    background:
      radial-gradient(ellipse 260px 140px at 330px 200px, rgba(80,120,255,0.55), transparent 70%),
      radial-gradient(ellipse 200px 120px at 120px 90px, rgba(60,100,240,0.45), transparent 70%),
      radial-gradient(ellipse 180px 110px at 260px 380px, rgba(50,90,230,0.4), transparent 70%);
  }

  .brand {
    position: absolute; left: 40px; top: 200px; width: 420px;
    font-weight: 700; font-size: 58px; line-height: 1; color: var(--ink-white);
    display: flex; align-items: center; gap: 14px;
  }
  .brand-dot { width: 22px; height: 22px; border-radius: 50%; background: var(--ink-white); flex: none; }

  .panel-header {
    position: absolute; top: 21px; height: 48px;
    background: linear-gradient(var(--header-fill-top), var(--header-fill-bottom));
    color: var(--header-ink); font-weight: 700; font-size: 22px;
    display: flex; align-items: center; justify-content: center;
  }
  .panel-header::after {
    content: ""; position: absolute; bottom: -11px; left: 50%; transform: translateX(-50%);
    border-left: 12px solid transparent; border-right: 12px solid transparent;
    border-top: 12px solid var(--header-fill-bottom);
  }
  .uses-header { left: 546px; width: 216px; }
  .features-header { left: 806px; width: 237px; }

  .uses-divider { position: absolute; left: 644px; top: 86px; width: 1px; height: 330px; background: var(--rule); }
  .use {
    position: absolute; width: 130px; text-align: center;
    font-size: 14px; line-height: 1.2;
  }
  .use svg { display: block; margin: 0 auto 6px; }

  .feature-list { position: absolute; left: 806px; top: 104px; list-style: none; }
  .feature-list li {
    display: flex; align-items: center; gap: 16px; height: 52px;
    font-weight: 700; font-size: 18px;
  }
  .feature-list svg { flex: none; }

  .sheet-rule-v { position: absolute; left: 1061px; top: 160px; width: 1px; height: 244px; background: var(--rule); }
  .sheet-rule-h { position: absolute; height: 1px; background: var(--rule); }
  .sheet-count { position: absolute; left: 1064px; width: 120px; text-align: center; }
  .sheet-count .num { font-size: 44px; font-weight: 400; line-height: 1; }
  .sheet-count .unit { font-size: 17px; font-weight: 500; margin-top: 4px; }
  .sheet-size { position: absolute; left: 1064px; top: 290px; width: 124px; text-align: center; font-size: 16px; font-weight: 700; line-height: 1.3; }

  .story-title { position: absolute; left: 53px; top: 420px; font-size: 22px; font-weight: 700; font-style: italic; }
  .story {
    position: absolute; top: 450px; font-size: 15.6px; line-height: 21px;
    text-align: justify;
  }
  .story-left { left: 53px; width: 566px; }
  .story-right { left: 644px; width: 542px; top: 446px; }
</style>
</head>
<body>
<main class="label">
  <div class="backdrop-photo" role="img" aria-label="Close-up of a soft blue scrubbing towel texture with floating bacteria"></div>

  <div class="brand"><span class="brand-dot"></span>Quirra Wipe</div>

  <div class="panel-header uses-header">Multipurpose Use</div>
  <div class="panel-header features-header">Features</div>

  <div class="uses-divider"></div>

  <div class="use" style="left:513px;top:86px">
    <svg width="56" height="50" viewBox="0 0 56 50" fill="none" stroke="#fff" stroke-width="2.5"><ellipse cx="26" cy="28" rx="22" ry="12"/><ellipse cx="26" cy="28" rx="12" ry="6"/><path d="M46 6l2 4 4 2-4 2-2 4-2-4-4-2 4-2z" fill="#fff" stroke="none"/></svg>
    Dishwashing
  </div>
  <div class="use" style="left:651px;top:80px">
    <svg width="56" height="56" viewBox="0 0 56 56" fill="none" stroke="#fff" stroke-width="2.5"><rect x="8" y="20" width="36" height="30" rx="2"/><line x1="8" y1="30" x2="44" y2="30"/><rect x="16" y="36" width="20" height="9"/><path d="M46 4l2 4 4 2-4 2-2 4-2-4-4-2 4-2z" fill="#fff" stroke="none"/></svg>
    Wiping<br>Down Stoves
  </div>
  <div class="use" style="left:513px;top:180px">
    <svg width="56" height="60" viewBox="0 0 56 60" fill="none" stroke="#fff" stroke-width="2.5"><rect x="14" y="6" width="22" height="16" rx="2"/><path d="M8 26h36c0 10-8 16-18 16S8 36 8 26z"/><path d="M18 42l-2 12h20l-2-12"/><path d="M48 10l2 4 4 2-4 2-2 4-2-4-4-2 4-2z" fill="#fff" stroke="none"/></svg>
    Cleaning<br>Toilets
  </div>
  <div class="use" style="left:651px;top:180px">
    <svg width="56" height="60" viewBox="0 0 56 60" fill="none" stroke="#fff" stroke-width="2.5"><path d="M8 22h38c0 12-8 18-19 18S8 34 8 22z"/><path d="M22 40v14h10V40"/><path d="M20 22V10h12"/><path d="M48 6l2 4 4 2-4 2-2 4-2-4-4-2 4-2z" fill="#fff" stroke="none"/></svg>
    Cleaning<br>Sinks
  </div>
  <div class="use" style="left:513px;top:314px">
    <svg width="56" height="56" viewBox="0 0 56 56" fill="none" stroke="#fff" stroke-width="2.5"><path d="M10 16h34M10 26h34M10 36h34M10 46h34M16 10v42M26 10v42M36 10v42"/><path d="M48 4l2 4 4 2-4 2-2 4-2-4-4-2 4-2z" fill="#fff" stroke="none"/></svg>
    Cleaning<br>Grills
  </div>
  <div class="use" style="left:651px;top:314px">
    <svg width="56" height="56" viewBox="0 0 56 56" fill="none" stroke="#fff" stroke-width="2.5"><ellipse cx="27" cy="26" rx="18" ry="6"/><path d="M9 26l4 20h28l4-20"/><path d="M46 8l2 4 4 2-4 2-2 4-2-4-4-2 4-2z" fill="#fff" stroke="none"/></svg>
    Cleaning<br>Pet Bowls
  </div>

  <ul class="feature-list">
    <li><svg width="22" height="30" viewBox="0 0 22 30"><path d="M22 0A15 15 0 0 0 22 30z" fill="#fff"/></svg>Perforated for Easy Tear</li>
    <li><svg width="22" height="30" viewBox="0 0 22 30"><path d="M22 0A15 15 0 0 0 22 30z" fill="#fff"/></svg>Reusable</li>
    <li><svg width="22" height="30" viewBox="0 0 22 30"><path d="M22 0A15 15 0 0 0 22 30z" fill="#fff"/></svg>Liquid Absorbent</li>
    <li><svg width="22" height="30" viewBox="0 0 22 30"><path d="M22 0A15 15 0 0 0 22 30z" fill="#fff"/></svg>Non-Flammable</li>
    <li><svg width="22" height="30" viewBox="0 0 22 30"><path d="M22 0A15 15 0 0 0 22 30z" fill="#fff"/></svg>Cadmium Free</li>
    <li><svg width="22" height="30" viewBox="0 0 22 30"><path d="M22 0A15 15 0 0 0 22 30z" fill="#fff"/></svg>Kitchen Safe</li>
  </ul>

  <div class="sheet-rule-v"></div>
  <div class="sheet-rule-h" style="left:1022px;top:160px;width:39px"></div>
  <div class="sheet-rule-h" style="left:1022px;top:403px;width:39px"></div>
  <div class="sheet-rule-h" style="left:1064px;top:254px;width:122px"></div>
  <div class="sheet-count" style="top:160px"><div class="num">60</div><div class="unit">Sheets</div></div>
  <div class="sheet-size">7.9" X 8.7"<br>per sheet</div>

  <h2 class="story-title">Did you know?</h2>
  <p class="story story-left">Sponges are the perfect place for bacteria growth! We're talking hundreds of different species of bacteria growing in your dishwashing sponge - just as bad as the inside of your toilet. So why use a dirty sponge over and over again? Why does it smell so bad? Yes your toilet is gross, but why should the sponge go overlooked?</p>
  <p class="story story-right">The Quirra Wipe is a sanitary solution to this problem. Use it once, wash and reuse up to three times before throwing each sheet away - that's enough for 180 washes per roll! But don't limit yourself to dishwashing. It's great for scrubbing surfaces with hardened debris or even dry residue left from old spills. So go ahead, take a stand against bacteria and wash away knowing your kitchen is finally clean. Now that's sanitary!</p>
</main>
</body>
</html>
```